Tomasi's Pizzeria BOGO Promotion Pizza Flyer (Huron)

Pizzeria flyer promoting "under new management" and then the main point for this flyer is our Buy One Get One Free promotion on our pizzas (disclaimer: not valid for Jr Family Crust or Family Pizzas)(we reserve the right to cancel this promotion at any time)
This promotion has no limit and can be carryout or delivery. No coupon needed.
Looking for a fun bright flyer with our logo colors

Requirements
Must have
• Store Info
• 287 Marwick Rd. E
• Dunmore, PA
• 555-562-3870
• Open at 4pm Daily!

```html
<!DOCTYPE html>
<html lang="en">
<head>
<meta charset="utf-8">
<title>Tomasi's Pizzeria – Buy One Get One Free</title>
<link rel="stylesheet" href="https://fonts.googleapis.com/css2?family=Oswald:wght@500;700&family=Roboto+Condensed:wght@700&family=Roboto:wght@400;700&display=swap">
<style>
  :root {
    --red: #d7161d;
    --red-dark: #a80f14;
    --yellow: #f6c319;
    --yellow-deep: #f0a90c;
    --ink: #161616;
    --paper: #f4f4f4;
    --white: #ffffff;
    --stage: #2a2624;
  }
  * { box-sizing: border-box; margin: 0; padding: 0; }
  html, body { width: 1200px; height: 900px; overflow: hidden; }
  body {
    background: var(--stage);
    font-family: "Roboto", Arial, sans-serif;
    position: relative;
  }
  .flyer {
    position: absolute;
    left: 290px; top: 18px;
    width: 620px; height: 864px;
    background: var(--paper);
    overflow: hidden;
  }
  .headline {
    position: absolute;
    left: 0; right: 0; top: 44px;
    display: flex; justify-content: center; align-items: center; gap: 14px;
    font-family: "Oswald", "Arial Narrow", sans-serif;
    text-transform: uppercase;
  }
  .headline-lines {
    color: var(--ink);
    font-weight: 700;
    font-size: 56px;
    line-height: 58px;
    letter-spacing: -1px;
  }
  .headline-free {
    color: var(--red);
    font-weight: 700;
    font-size: 128px;
    line-height: 116px;
    letter-spacing: -2px;
  }
  .disclaimer {
    position: absolute;
    left: 94px; right: 94px; top: 176px; height: 48px;
    border-top: 2px dashed #555;
    border-bottom: 2px dashed #555;
    text-align: center;
    font-size: 13px; line-height: 20px;
    color: var(--ink);
    padding-top: 3px;
  }
  .disclaimer strong { font-weight: 700; }
  .hours {
    position: absolute;
    left: 150px; width: 320px; top: 234px; height: 58px;
    background: var(--yellow);
    border-radius: 6px 18px 8px 20px;
    box-shadow: -8px 2px 0 var(--yellow-deep), 8px -2px 0 var(--yellow-deep);
    font-family: "Roboto Condensed", Arial, sans-serif;
    font-weight: 700;
    font-size: 34px;
    line-height: 58px;
    text-align: center;
    color: var(--ink);
  }
  .hours em { font-style: normal; color: var(--red); }
  .food-photo {
    position: absolute;
    left: 0; top: 304px; width: 620px; height: 524px;
    background:
      radial-gradient(ellipse 300px 150px at 55% 58%, #c88a45 0%, #8e5a2a 45%, #3d2a1e 75%, transparent 100%),
      linear-gradient(180deg, #55504b 0%, #3a342f 50%, #1e1a17 100%);
  }
  .header-point {
    position: absolute; left: 0; top: 300px;
    width: 620px; height: 120px;
  }
  .feature-icon {
    position: absolute; top: 318px;
    width: 78px; height: 88px;
  }
  .feature-icon.drink { left: 71px; }
  .feature-icon.pizza { left: 471px; }
  .brand-badge {
    position: absolute;
    left: 215px; top: 326px;
    width: 190px; height: 190px;
  }
  .brand-name {
    position: absolute;
    left: 215px; top: 326px; width: 190px; height: 190px;
    display: flex; flex-direction: column; align-items: center; justify-content: center;
    gap: 10px;
    font-family: "Oswald", "Arial Narrow", sans-serif;
    font-weight: 700;
    font-size: 24px;
    line-height: 26px;
    text-align: center;
    color: var(--red);
    text-transform: uppercase;
  }
  .brand-dot {
    width: 18px; height: 18px; border-radius: 50%;
    background: var(--red);
  }
  .bottom-band {
    position: absolute;
    left: 0; right: 0; top: 828px; height: 36px;
    background: var(--yellow-deep);
  }
  .store-bar {
    position: absolute;
    left: 14px; right: 14px; top: 772px; height: 56px;
    background: var(--red);
    display: grid;
    grid-template-columns: 1fr 1fr 1fr;
    align-items: center;
    color: var(--white);
    text-align: center;
  }
  .store-address, .store-contact { font-size: 12px; line-height: 17px; }
  .store-call { border-left: 1px solid rgba(255,255,255,.5); border-right: 1px solid rgba(255,255,255,.5); }
  .store-call-label { font-size: 13px; font-weight: 700; letter-spacing: .5px; }
  .store-call-number { font-size: 24px; font-weight: 700; line-height: 28px; }
  .pin-marker {
    position: absolute; top: 752px;
    width: 30px; height: 34px;
    z-index: 2;
  }
  .pin-marker.left { left: 86px; }
  .pin-marker.right { left: 504px; }
</style>
</head>
<body>
<main class="flyer">
  <h1 class="headline">
    <span class="headline-lines">Buy One<br>Get One</span>
    <span class="headline-free">Free</span>
  </h1>

  <p class="disclaimer"><strong>Disclaimer:</strong> not valid for Jr Family Crust or Family Pizzas<br>we reserve the right to cancel this promotion at any time</p>

  <p class="hours">Open at <em>4pm</em> Daily!</p>

  <div class="food-photo" role="img" aria-label="Photo of a pizza with olives, vegetables and cheese in a cast-iron pan"></div>

  <svg class="header-point" viewBox="0 0 620 120" aria-hidden="true">
    <polygon points="0,0 620,0 620,22 310,112 0,22" fill="var(--paper)"/>
  </svg>

  <svg class="feature-icon drink" viewBox="0 0 78 88" aria-hidden="true">
    <polygon points="39,0 78,22 78,66 39,88 0,66 0,22" fill="var(--red)"/>
    <path d="M27 30 H51 L47 62 H31 Z" fill="none" stroke="#fff" stroke-width="3" stroke-linejoin="round"/>
    <path d="M29.5 42 H48.5 L47 58 H31 Z" fill="var(--yellow)"/>
    <line x1="44" y1="22" x2="40" y2="38" stroke="#fff" stroke-width="3" stroke-linecap="round"/>
  </svg>

  <svg class="feature-icon pizza" viewBox="0 0 78 88" aria-hidden="true">
    <polygon points="39,0 78,22 78,66 39,88 0,66 0,22" fill="var(--red)"/>
    <circle cx="39" cy="44" r="18" fill="#fff"/>
    <path d="M39 44 L57 44 A18 18 0 0 1 39 62 Z" fill="var(--yellow)"/>
    <circle cx="32" cy="38" r="3" fill="var(--red)"/>
    <circle cx="44" cy="34" r="3" fill="var(--red)"/>
    <circle cx="31" cy="51" r="3" fill="var(--red)"/>
  </svg>

  <svg class="brand-badge" viewBox="0 0 190 190" aria-hidden="true">
    <polygon points="95,2 177,49 177,141 95,188 13,141 13,49" fill="var(--white)"/>
  </svg>
  <div class="brand-name">
    <span class="brand-dot"></span>
    <span>Tomasi's<br>Pizzeria</span>
  </div>

  <div class="bottom-band"></div>

  <section class="store-bar">
    <p class="store-address">287 Marwick Rd.<br>E- Dunmore, PA</p>
    <p class="store-call">
      <span class="store-call-label">CALL OUT</span><br>
      <span class="store-call-number">555-562-3870</span>
    </p>
    <p class="store-contact">Phone : +555-562-3870<br>email : orders@tomasis.example</p>
  </section>

  <svg class="pin-marker left" viewBox="0 0 30 34" aria-hidden="true">
    <polygon points="15,0 30,8.5 30,25.5 15,34 0,25.5 0,8.5" fill="var(--red)"/>
    <path d="M15 9 a5 5 0 0 1 5 5 c0 4 -5 9 -5 9 s-5 -5 -5 -9 a5 5 0 0 1 5 -5z" fill="#fff"/>
    <circle cx="15" cy="14" r="1.8" fill="var(--red)"/>
  </svg>
  <svg class="pin-marker right" viewBox="0 0 30 34" aria-hidden="true">
    <polygon points="15,0 30,8.5 30,25.5 15,34 0,25.5 0,8.5" fill="var(--red)"/>
    <circle cx="15" cy="17" r="7" fill="none" stroke="#fff" stroke-width="2"/>
    <path d="M8 17 H22 M15 10 C11 14 11 20 15 24 M15 10 C19 14 19 20 15 24" fill="none" stroke="#fff" stroke-width="1.5"/>
  </svg>
</main>
</body>
</html>
```